Business Card Design

I would like a simple logo for Marwick Holdings.
We run a company that looks after our extended
family's investments.

Industry/Entity Type

Business

Contact Information for Business Card

Colleen Barfoot
Director
Marwick Holdings
ABN 72 318 506 942
Investment Management
colleen@marwickholdings.com.au
Mobile +61 437 880 642
Level 1, 57 Paxton St
Townsville, Qld 4810

```html
<!DOCTYPE html>
<html lang="en">
<head>
<meta charset="utf-8">
<title>Marwick Holdings – Business Card</title>
<link href="https://fonts.googleapis.com/css2?family=Source+Sans+3:wght@400;600;700&display=swap" rel="stylesheet">
<style>
  :root {
    --page-bg: #d4d4d6;
    --charcoal: #333335;
    --silver: #c1c1c1;
    --brand-blue: #2f80c9;
    --ink: #2a2a2a;
    --white: #ffffff;
  }
  * { box-sizing: border-box; margin: 0; padding: 0; }
  html, body {
    width: 883px; height: 1200px; overflow: hidden;
    background: var(--page-bg);
    font-family: "Source Sans 3", "Myriad Pro", sans-serif;
  }
  .stage {
    width: 883px; height: 1200px;
    display: flex; flex-direction: column; align-items: center; justify-content: center;
    gap: 16px;
  }
  .card {
    position: relative;
    width: 390px; height: 219px;
    background: var(--charcoal);
    box-shadow: 0 6px 8px rgba(0,0,0,0.22);
    overflow: hidden;
  }
  .card__top-band { position: absolute; left: 0; top: 0; width: 100%; height: 24px; background: var(--charcoal); }
  .card__rule { position: absolute; left: 0; width: 100%; height: 2px; background: var(--brand-blue); }
  .card__rule--upper { top: 25px; }
  .card__rule--lower { top: 124px; }
  .card__identity { position: absolute; left: 0; top: 27px; width: 100%; height: 97px; background: var(--silver); }
  .card__foot-band { position: absolute; left: 0; bottom: 0; width: 100%; height: 19px; background: var(--brand-blue); }

  .brand { position: absolute; left: 18px; top: 10px; }
  .brand__dot {
    display: block; width: 44px; height: 44px; margin-left: 30px; margin-bottom: 11px;
    border-radius: 50%; border: 2px solid var(--brand-blue);
  }
  .brand__name { font-size: 17px; font-weight: 700; color: var(--ink); letter-spacing: 0.1px; white-space: nowrap; }

  .person { position: absolute; right: 18px; top: 20px; text-align: right; line-height: 1.1; }
  .person__name { font-size: 13px; color: var(--brand-blue); }
  .person__role { font-size: 10px; color: var(--ink); }

  .company-meta { position: absolute; left: 20px; top: 134px; font-size: 10.5px; line-height: 13px; color: var(--brand-blue); }

  .contact { position: absolute; right: 20px; top: 153px; list-style: none; }
  .contact__item {
    display: flex; align-items: center; justify-content: flex-end; gap: 7px;
    font-size: 10px; line-height: 14.5px; color: var(--white);
  }
  .contact__icon { width: 9px; height: 9px; fill: var(--brand-blue); flex: none; }
</style>
</head>
<body>
<main class="stage">
  <article class="card">
    <div class="card__top-band"></div>
    <div class="card__rule card__rule--upper"></div>
    <section class="card__identity">
      <div class="brand">
        <span class="brand__dot"></span>
        <p class="brand__name">Marwick Holdings</p>
      </div>
      <div class="person">
        <p class="person__name">Colleen Barfoot</p>
        <p class="person__role">Director</p>
      </div>
    </section>
    <div class="card__rule card__rule--lower"></div>
    <div class="company-meta">
      <p>ABN 72 318 506 942</p>
      <p>Investment Management</p>
    </div>
    <ul class="contact">
      <li class="contact__item">+61 437 880 642
        <svg class="contact__icon" viewBox="0 0 10 10"><path d="M1 3.5C1 2 3 1.5 5 1.5S9 2 9 3.5L7.3 4 6.8 3H3.2L2.7 4Z"/><rect x="2" y="4.5" width="6" height="4" rx="0.6"/></svg>
      </li>
      <li class="contact__item">colleen@marwickholdings.com.au
        <svg class="contact__icon" viewBox="0 0 10 10"><rect x="0.5" y="2" width="9" height="6" rx="0.6"/></svg>
      </li>
      <li class="contact__item">Level 1, 57 Paxton St Townsville, Qld 4810
        <svg class="contact__icon" viewBox="0 0 10 10"><path d="M5 0.5A3.2 3.2 0 0 0 1.8 3.7C1.8 6.2 5 9.5 5 9.5S8.2 6.2 8.2 3.7A3.2 3.2 0 0 0 5 0.5Zm0 4.6A1.3 1.3 0 1 1 5 2.5a1.3 1.3 0 0 1 0 2.6Z"/></svg>
      </li>
    </ul>
    <div class="card__foot-band"></div>
  </article>

  <article class="card">
    <div class="card__top-band"></div>
    <div class="card__rule card__rule--upper"></div>
    <section class="card__identity">
      <div class="brand">
        <span class="brand__dot"></span>
        <p class="brand__name">Marwick Holdings</p>
      </div>
      <div class="person">
        <p class="person__name">Colleen Barfoot</p>
        <p class="person__role">Director</p>
      </div>
    </section>
    <div class="card__rule card__rule--lower"></div>
    <div class="company-meta">
      <p>ABN 72 318 506 942</p>
      <p>Investment Management</p>
    </div>
    <ul class="contact">
      <li class="contact__item">+61 437 880 642
        <svg class="contact__icon" viewBox="0 0 10 10"><path d="M1 3.5C1 2 3 1.5 5 1.5S9 2 9 3.5L7.3 4 6.8 3H3.2L2.7 4Z"/><rect x="2" y="4.5" width="6" height="4" rx="0.6"/></svg>
      </li>
      <li class="contact__item">colleen@marwickholdings.com.au
        <svg class="contact__icon" viewBox="0 0 10 10"><rect x="0.5" y="2" width="9" height="6" rx="0.6"/></svg>
      </li>
      <li class="contact__item">Level 1, 57 Paxton St Townsville, Qld 4810
        <svg class="contact__icon" viewBox="0 0 10 10"><path d="M5 0.5A3.2 3.2 0 0 0 1.8 3.7C1.8 6.2 5 9.5 5 9.5S8.2 6.2 8.2 3.7A3.2 3.2 0 0 0 5 0.5Zm0 4.6A1.3 1.3 0 1 1 5 2.5a1.3 1.3 0 0 1 0 2.6Z"/></svg>
      </li>
    </ul>
    <div class="card__foot-band"></div>
  </article>
</main>
</body>
</html>
```